Shopguidecraft.com

I've attached two different logo's which I both like and would like to see different designs with each logo. I'm starting a retail consulting business and blog. You can view the start of my project at shopguidecraft.com to get an idea of what I'm creating.
Looking for a design that says creative, strategic and community.
Updates
Hello Everyone,
Thank you for the amazing design so far.
What I Like
- double sided designs, front and back
- one side should be white or green. Customers cannot write on or make notes on an all black card
- Simple, cool, creative is best
My business card will only have the following
- Instagram
- Facebook
- Email
- Website
My new Tag line is
Think Smart. Lead Smart. Work Smart.
My title will be:
Dorian Kessel
Retail Consultant
Please submit 1 or 2 designs with these specifications.
Thank you,
Dorian
Reason: Looking for a few more designs and have now committed the project and it is no longer refundable. Please read brief and follow specific instructions.
Looking for something simple yet creative. Something that may stand out from most cards.
Thank you,
Dorian
Thank you,
Dorian
Target Market(s)
My main target is retail managers and retail businesses that are focused on leadership and people development.
Industry/Entity Type
Retail
Look and feel
Each slider illustrates characteristics of the customer's brand and the style your logo design should communicate.

```html
<!DOCTYPE html>
<html lang="en">
<head>
<meta charset="utf-8">
<title>Shopguidecraft.com – Business Card</title>
<link rel="stylesheet" href="https://fonts.googleapis.com/css2?family=Questrial&family=Montserrat:wght@600;700&display=swap">
<style>
  :root {
    --page-bg: #e4e4e4;
    --card-black: #1b1b1c;
    --card-white: #ffffff;
    --brand-green: #7cc221;
    --ink-dark: #232323;
    --ink-muted: #bdbdbd;
    --ink-white: #ffffff;
  }
  * { box-sizing: border-box; margin: 0; padding: 0; }
  html, body { width: 1200px; height: 900px; overflow: hidden; }
  body {
    background: var(--page-bg);
    display: flex;
    flex-direction: column;
    align-items: center;
    justify-content: center;
    gap: 40px;
    font-family: "Montserrat", Arial, sans-serif;
  }
  .card {
    position: relative;
    width: 700px;
    height: 400px;
    border-radius: 26px;
    overflow: hidden;
    box-shadow: 0 8px 24px rgba(0,0,0,.18);
  }

  /* Brand lockup */
  .brand { display: flex; flex-direction: column; align-items: flex-start; }
  .brand-row { display: flex; align-items: center; gap: 14px; }
  .brand-dot { border-radius: 50%; background: var(--brand-green); flex: none; }
  .brand-name {
    font-family: "Questrial", Arial, sans-serif;
    color: var(--ink-white);
    letter-spacing: -0.5px;
    line-height: 1;
    white-space: nowrap;
  }
  .brand-tagline {
    font-weight: 700;
    color: var(--ink-muted);
    text-transform: uppercase;
    white-space: nowrap;
  }

  /* Back */
  .card-back { background: var(--card-black); }
  .card-back .brand { position: absolute; left: 74px; top: 136px; }
  .card-back .brand-dot { width: 62px; height: 62px; }
  .card-back .brand-name { font-size: 50px; }
  .card-back .brand-tagline { font-size: 14px; letter-spacing: 4.2px; margin-top: 14px; margin-left: 76px; }

  /* Front */
  .card-front { background: var(--card-white); }
  .front-band {
    position: absolute; left: 0; top: 0; width: 100%; height: 118px;
    background: var(--card-black);
    border-bottom: 6px solid var(--brand-green);
  }
  .card-front .brand { position: absolute; right: 36px; top: 24px; align-items: flex-end; }
  .card-front .brand-dot { width: 44px; height: 44px; }
  .card-front .brand-name { font-size: 34px; }
  .card-front .brand-tagline { font-size: 10px; letter-spacing: 3px; margin-top: 10px; }

  .front-bottom-rule {
    position: absolute; left: 0; bottom: 0; width: 100%; height: 18px;
    background: var(--card-black);
    border-top: 4px solid var(--brand-green);
  }

  .person { position: absolute; left: 48px; top: 150px; }
  .person-name {
    font-family: "Questrial", Arial, sans-serif;
    font-size: 34px; font-weight: 400; color: var(--brand-green); line-height: 1.05;
  }
  .person-title {
    font-family: "Questrial", Arial, sans-serif;
    font-size: 20px; color: var(--ink-dark);
  }

  .contacts {
    position: absolute; left: 340px; top: 150px;
    list-style: none; display: flex; flex-direction: column; gap: 14px;
  }
  .contact { display: flex; align-items: center; gap: 12px; font-size: 15px; font-weight: 600; color: var(--ink-dark); white-space: nowrap; }
  .contact-icon { width: 30px; height: 30px; flex: none; }
</style>
</head>
<body>

<section class="card card-back" aria-label="Card back">
  <div class="brand">
    <div class="brand-row">
      <span class="brand-dot"></span>
      <span class="brand-name">Shopguidecraft.com</span>
    </div>
    <p class="brand-tagline">Plan Well · Guide Well · Grow Well</p>
  </div>
</section>

<section class="card card-front" aria-label="Card front">
  <div class="front-band"></div>
  <div class="brand">
    <div class="brand-row">
      <span class="brand-dot"></span>
      <span class="brand-name">Shopguidecraft.com</span>
    </div>
    <p class="brand-tagline">Plan Well · Guide Well · Grow Well</p>
  </div>

  <div class="person">
    <h1 class="person-name">Dorian Kessel</h1>
    <p class="person-title">Retail Consultant</p>
  </div>

  <ul class="contacts">
    <li class="contact">
      <svg class="contact-icon" viewBox="0 0 30 30" aria-hidden="true">
        <rect width="30" height="30" rx="6" fill="#1b1b1c"/>
        <g fill="none" stroke="#fff" stroke-width="1.6">
          <circle cx="15" cy="15" r="9"/>
          <ellipse cx="15" cy="15" rx="4" ry="9"/>
          <line x1="6" y1="15" x2="24" y2="15"/>
          <line x1="7.5" y1="10.5" x2="22.5" y2="10.5"/>
          <line x1="7.5" y1="19.5" x2="22.5" y2="19.5"/>
        </g>
      </svg>
      www.shopguidecraft.com
    </li>
    <li class="contact">
      <svg class="contact-icon" viewBox="0 0 30 30" aria-hidden="true">
        <rect width="30" height="30" rx="6" fill="#1b1b1c"/>
        <g fill="none" stroke="#fff" stroke-width="1.6" stroke-linejoin="round">
          <rect x="6" y="9" width="18" height="12"/>
          <polyline points="6,9 15,16 24,9"/>
        </g>
      </svg>
      Dorian@shopguidecraft.com
    </li>
    <li class="contact">
      <svg class="contact-icon" viewBox="0 0 30 30" aria-hidden="true">
        <rect width="30" height="30" rx="6" fill="#1b1b1c"/>
      </svg>
      hubline.net/shopguidecraft
    </li>
    <li class="contact">
      <svg class="contact-icon" viewBox="0 0 30 30" aria-hidden="true">
        <rect width="30" height="30" rx="6" fill="#1b1b1c"/>
      </svg>
      linkroster.net/dorian-kessel
    </li>
  </ul>

  <div class="front-bottom-rule"></div>
</section>

</body>
</html>
```